One of Australia's fastest growing Financial Company looking for an updated business card design!

Meridale Holdings Australia is looking for an updated design for our business cards. We would like to keep up our professional appearances and have get new exciting design that fits our company.

The Meridale aim is to facilitate and assist clients in every financial requirement that may arise in financial areas.

We would to see the design to use colour blue and we like the clouds in the background. We have attached two designs we have use before but we need something with more professional and easy to read design.

We would like the website in the back of the card; the employees name more central and stands out; only a postal address; a list of all our locations along the bottom (Sydney, Melbourne, Brisbane, Singapore)

Looking forward to seeing the designs come in!

Target Market(s)

Other Industry Professionals
Middle Class Families

Industry/Entity Type

Finance

Contact Information for Business Card

Name; Company Role; Office Number; Mobile Number; Email Address; Website; Postal Address; Locations

Font styles to use
Serif
Sans Serif

Colors
0492cd
33a6d7
85cae6
85acd3
3176b5
0455a3
cee9f5
d5e2ee

Requirements
Must have
• Name; Company Role; Office Number; Mobile Number; Email Address; Website; Postal Address; Locations
Nice to have
• The colour blue, clouds on the background

```html
<!DOCTYPE html>
<html lang="en">
<head>
<meta charset="utf-8">
<title>Meridale Holdings Australia – Business Card</title>
<link rel="stylesheet" href="https://fonts.googleapis.com/css2?family=Open+Sans:wght@400;600;700&display=swap">
<style>
  :root {
    --blue-deep: #0455a3;
    --blue-mid: #3176b5;
    --blue-bright: #0492cd;
    --blue-sky: #33a6d7;
    --blue-pale: #cee9f5;
    --accent-red: #e0262b;
    --ink: #3a3a3a;
    --paper: #ffffff;
    --backdrop: #e9edf1;
  }
  * { box-sizing: border-box; margin: 0; padding: 0; }
  html, body {
    width: 1200px; height: 950px; overflow: hidden;
    background: var(--backdrop);
    font-family: "Open Sans", Arial, sans-serif;
  }
  .sheet {
    width: 1200px; height: 950px;
    display: flex; flex-direction: column; align-items: center; justify-content: center; gap: 50px;
  }
  .card {
    position: relative; width: 700px; height: 400px; overflow: hidden;
    box-shadow: 0 6px 20px rgba(0,0,0,.18);
  }

  /* Back side */
  .card--back {
    background: radial-gradient(ellipse at 70% 30%, var(--blue-sky) 0%, var(--blue-bright) 40%, var(--blue-deep) 100%);
  }
  .card--back .brand {
    position: absolute; left: 0; right: 0; top: 150px;
    display: flex; align-items: center; justify-content: center; gap: 18px;
  }
  .card--back .brand-mark {
    width: 46px; height: 46px; border-radius: 50%; background: var(--paper);
  }
  .card--back .brand-name {
    font-size: 72px; font-weight: 600; color: var(--paper); letter-spacing: 1px;
  }
  .locations {
    position: absolute; right: 40px; bottom: 36px;
    color: var(--paper); font-size: 17px; letter-spacing: .5px;
  }
  .locations .dot { margin: 0 8px; }

  /* Front side */
  .card--front { background: var(--paper); }
  .card--front .brand {
    position: absolute; right: 40px; top: 60px;
    display: flex; align-items: center; gap: 14px;
  }
  .card--front .brand-mark {
    width: 40px; height: 40px; border-radius: 50%; background: var(--accent-red);
  }
  .card--front .brand-name {
    font-size: 56px; font-weight: 600; color: var(--blue-mid);
  }
  .person { position: absolute; left: 40px; top: 92px; }
  .person-name { font-size: 30px; font-weight: 700; color: var(--blue-mid); line-height: 1.1; }
  .person-role { font-size: 19px; font-weight: 700; color: var(--accent-red); }
  .contacts {
    position: absolute; left: 40px; top: 180px;
    list-style: none; font-size: 18px; color: var(--ink); line-height: 1.55;
  }
  .contacts li { display: flex; align-items: center; gap: 8px; }
  .contacts svg { width: 18px; height: 18px; fill: var(--blue-bright); }
  .divider {
    position: absolute; left: 300px; right: 40px; top: 282px;
    height: 1px; background: var(--accent-red);
  }
  .address {
    position: absolute; right: 40px; top: 296px;
    font-style: normal; text-align: right; font-size: 18px; color: var(--ink); line-height: 1.4;
  }
  .footer-band {
    position: absolute; left: 0; right: 0; bottom: 0; height: 12px;
    background: var(--blue-bright); border-top: 3px solid var(--accent-red);
  }
</style>
</head>
<body>
<main class="sheet">
  <section class="card card--back" aria-label="Card back">
    <div class="brand">
      <span class="brand-mark"></span>
      <span class="brand-name">Meridale</span>
    </div>
    <p class="locations">Sydney<span class="dot">•</span>Melbourne<span class="dot">•</span>Brisbane<span class="dot">•</span>Singapore</p>
  </section>

  <section class="card card--front" aria-label="Card front">
    <div class="brand">
      <span class="brand-mark"></span>
      <span class="brand-name">Meridale</span>
    </div>
    <div class="person">
      <h1 class="person-name">Claire Hollis</h1>
      <p class="person-role">Investment Consultant</p>
    </div>
    <ul class="contacts">
      <li>
        <svg viewBox="0 0 24 24" aria-hidden="true"><path d="M6.6 10.8a15 15 0 0 0 6.6 6.6l2.2-2.2c.3-.3.7-.4 1-.2 1.1.4 2.3.6 3.6.6.6 0 1 .4 1 1V20c0 .6-.4 1-1 1A17 17 0 0 1 3 4c0-.6.4-1 1-1h3.5c.6 0 1 .4 1 1 0 1.3.2 2.5.6 3.6.1.3 0 .7-.2 1z"/></svg>
        (02) 5550 1842
      </li>
      <li>
        <svg viewBox="0 0 24 24" aria-hidden="true"><path d="M7 2h10a2 2 0 0 1 2 2v16a2 2 0 0 1-2 2H7a2 2 0 0 1-2-2V4a2 2 0 0 1 2-2zm0 3v13h10V5z"/></svg>
        0400 555 218
      </li>
      <li>info@meridaleholdings.com.au</li>
    </ul>
    <div class="divider"></div>
    <address class="address">
      52 Elmwood Lane<br>
      Kingsford Bay, NSW 2450<br>
      www.meridaleholdings.com.au
    </address>
    <div class="footer-band"></div>
  </section>
</main>
</body>
</html>
```